Professional Website for Commercial Real Estate Broker

I own a small boutique commercial real estate company called Birchwell Holdings.
My current website is www.teamdurnio.com and is hosted on hostlark. I am looking for an all new website that will allow me to compete with bigger players in our industry. In other words, I need something professional, sleek, and functional.

I am looking for a designer that can take my complete website all the way to coding, migration, and launch. I understand that this may be an add'l charge, so please include with your design submission what the add'l charge will be to take the website to launch with all functionality as described below.

As an example of a page in my industry that I like please check out: www.marcusolverin.com.

My logo is attached and my main colors are the blue, white, grey - similar to the logo.

I am looking for a five page website with the following pages:

Home
Birchwell Team
Services
Sold Properties
Contact

A couple of features that I will want on the site are:

- I want to make sure that we can imbed a news commercial real estate news feed from: http://www.plazowire.com/news/ on the website's home page, similar to how it is on marcusolverin.com.

- Sold Properties page will allow me to upload the following information on to the website so that I can add new properties that I have recently sold on a weekly or monthly basis. I would like the information to be displayed similarly to http://www.marcusolverin.com/properties.html . I should be able to upload: picture, price, bldg size, lot size, closing date for each property. This will require a user friendly back end that I can navigate.

- On the home page, I also want to have a form where visitors can request a Market Analysis of their property by entering: Name, property address, email address, phone number. I will be sent an email with this information and I can follow up via telephone or email direct.

- The Birchwell Team page will have a picture, contact info, and brief bio for each member of the team. I would like to be able to adjust this on a user friendly back end.

I have included my Company Logo. Feel free to use any text from my current website: www.teamdurnio.com. Also, any sleek looking stock photos of office / commercial buildings can be used for the initial design purposes.

I look forward to getting your design submittal and moving forward asap!

Target Market(s)

Los Angeles real estate brokers, developers, and investors.

Industry/Entity Type

Real Estate

Coding

Coded - Design and coding required

Number of Pages Required

5+ page

Font styles to use
Sans Serif

Colors
ffffff
85abd2
0455a3
b2b2b2
000000
3276b5

Requirements
Must have
• Sleek and professional design.
• - I want to make sure that we can imbed a news commercial real estate news feed from: http://www.plazowire.com/news/ on the website's home page, similar to how it is on marcusolverin.com.
• - Sold Properties page will allow me to upload the following information on to the website so that I can add new properties that I have recently sold on a weekly or monthly basis. I would like the information to be displayed similarly to http://www.marcusolverin.com/properties.html . I should be able to upload: picture, price, bldg size, lot size, closing date for each property. This will require a user friendly back end that I can navigate.
• - On the home page, I also want to have a form where visitors can request a Market Analysis of their property by entering: Name, property address, email address, phone number. I will be sent an email with this information and I can follow up via telephone or email direct.
Nice to have
• Dynamic banner on the home page with beautiful photos that change every few seconds.

```html
<!DOCTYPE html>
<html lang="en">
<head>
<meta charset="utf-8">
<title>Birchwell Holdings — Commercial Real Estate</title>
<link rel="stylesheet" href="https://fonts.googleapis.com/css2?family=Lato:wght@400;700;900&family=Open+Sans:wght@400;600;700&display=swap">
<style>
:root{
  --blue:#0455a3;
  --blue-mid:#3276b5;
  --blue-light:#85abd2;
  --blue-deep:#0a4c92;
  --grey:#b2b2b2;
  --grey-soft:#f3f3f5;
  --field:#f1f1f1;
  --ink:#222;
  --text:#555;
  --white:#fff;
}
*{box-sizing:border-box;margin:0;padding:0}
html,body{width:1200px;height:2571px;overflow:hidden;background:var(--white)}
body{position:relative;font-family:"Open Sans",Arial,sans-serif;color:var(--text)}
.abs{position:absolute}
a{color:inherit;text-decoration:none}

/* header */
.site-header{position:absolute;left:0;top:0;width:1200px;height:135px;background:var(--white)}
.brand{position:absolute;left:100px;top:44px;display:flex;align-items:center;gap:12px}
.brand-square{width:34px;height:34px;background:var(--blue)}
.brand-name{font-family:"Lato",sans-serif;font-weight:900;font-size:26px;color:var(--blue);letter-spacing:.5px}
.header-phone{position:absolute;left:785px;top:29px;font-size:17px;color:#444;display:flex;align-items:center;gap:10px}
.btn{display:flex;align-items:center;justify-content:center;background:var(--blue);color:var(--white);font-family:"Lato",sans-serif;font-weight:700;border-radius:30px;letter-spacing:.6px}
.btn-quote{position:absolute;left:963px;top:23px;width:137px;height:36px;font-size:14px}
.main-nav{position:absolute;right:100px;top:81px;display:flex;gap:36px;font-family:"Lato",sans-serif;font-weight:700;font-size:16px;color:#222}
.main-nav .active{color:var(--blue);border-bottom:2px solid var(--blue);padding-bottom:6px}

/* hero */
.hero{position:absolute;left:0;top:135px;width:1200px;height:630px}
.hero-photo{position:absolute;inset:0;background:linear-gradient(100deg,#8d8a86 0%,#b9b6b1 25%,#d7d3cd 45%,#a59b8f 62%,#c9c4bc 75%,#3c3a38 88%,#6e6d6b 100%)}
.hero-title{position:absolute;left:0;width:1200px;top:238px;text-align:center;font-family:"Lato",sans-serif;font-weight:900;font-size:66px;color:var(--white);letter-spacing:1px;text-shadow:0 2px 6px rgba(0,0,0,.35)}
.hero-sub{position:absolute;left:0;width:1200px;top:343px;text-align:center;font-size:18px;font-weight:600;color:var(--white);text-shadow:0 1px 4px rgba(0,0,0,.35)}
.btn-ghost{position:absolute;left:529px;top:400px;width:140px;height:38px;border:2px solid var(--white);border-radius:30px;color:var(--white);font-family:"Lato",sans-serif;font-size:15px;display:flex;align-items:center;justify-content:center;letter-spacing:.5px}
.slider-arrow{position:absolute;top:248px;width:34px;height:34px;border-radius:50%;background:rgba(40,40,40,.6);display:flex;align-items:center;justify-content:center}
.slider-dots{position:absolute;top:545px;left:0;width:1200px;display:flex;justify-content:center;gap:7px}
.slider-dots span{width:12px;height:12px;border-radius:50%;border:2px solid var(--white)}
.slider-dots .on{background:var(--blue);border-color:var(--blue)}
.hero-edge{position:absolute;left:0;top:0;width:1200px;height:630px}

/* about */
.section-title{font-family:"Lato",sans-serif;font-weight:700;color:#222;letter-spacing:.5px}
.about-title{position:absolute;left:100px;top:830px;font-size:31px}
.about-photo{position:absolute;left:100px;top:903px;width:465px;height:258px;border:4px solid #eee;background:linear-gradient(120deg,#c9d6e0,#e8ecef 40%,#9aa7b3 70%,#d9d3cc)}
.about-text{position:absolute;left:100px;top:1203px;width:470px;font-size:12.5px;line-height:24px;color:#555}
.btn-more{position:absolute;left:100px;top:1336px;width:128px;height:42px;font-size:14px}

.analysis{position:absolute;left:623px;top:842px;width:477px;height:533px;border:5px solid #d0d0d0}
.analysis h2{position:absolute;left:0;width:467px;top:55px;text-align:center;font-family:"Lato",sans-serif;font-weight:700;font-size:20px;line-height:27px;color:#222;letter-spacing:.6px}
.field{position:absolute;left:38px;width:393px;height:41px;background:var(--field);border:1px solid #e2e2e2;font-size:13px;color:#777;padding:12px 18px}
.req{position:absolute;left:38px;top:394px;font-size:13px;color:#555}
.btn-submit{position:absolute;left:172px;top:423px;width:124px;height:43px;font-size:15px}

/* news */
.news-head{position:absolute;left:100px;top:1485px;width:1000px;height:62px;background:var(--blue);color:var(--white);font-family:"Lato",sans-serif;font-weight:700;font-size:25px;padding:15px 28px;letter-spacing:.5px}
.news-body{position:absolute;left:100px;top:1547px;width:1000px;height:453px}
.news-item{position:absolute;left:42px;width:920px;height:125px}
.news-thumb{position:absolute;left:0;top:0;width:203px;height:122px;border:1px solid #ddd}
.news-thumb.logo{background:var(--white);display:flex;align-items:center;justify-content:center;font-family:"Lato",sans-serif;font-weight:700;font-size:30px;color:#333}
.news-thumb.city{background:linear-gradient(160deg,#a9b9c6,#5f6f78 45%,#6d8a5a 80%,#8a8f84)}
.news-title{position:absolute;left:247px;top:6px;font-family:"Lato",sans-serif;font-weight:700;font-size:17px;color:var(--blue);letter-spacing:.5px}
.news-excerpt{position:absolute;left:247px;top:44px;font-size:12px;color:#555}
.news-date{position:absolute;left:247px;top:70px;font-size:12px;color:#555}
.news-more{position:absolute;left:247px;top:100px;font-family:"Lato",sans-serif;font-weight:700;font-size:13px;color:var(--blue);letter-spacing:.5px;display:flex;align-items:center;gap:5px}
.scroll-track{position:absolute;left:977px;top:0;width:23px;height:330px;background:#e3e3e3}
.scroll-thumb{position:absolute;left:977px;top:0;width:23px;height:90px;background:#c4c4c4}
.btn-news{position:absolute;left:518px;top:1907px;width:164px;height:44px;font-size:14px}

/* newsletter */
.news-title-lg{position:absolute;left:100px;top:2056px;font-size:26px}
.newsletter-sub{position:absolute;left:100px;top:2105px;font-size:12px;color:#666}
.signup{position:absolute;left:716px;top:2075px;width:383px;height:34px;border:1px solid #ddd;border-radius:20px;background:var(--white)}
.signup span{position:absolute;left:22px;top:8px;font-size:12px;color:#666}
.signup .send{position:absolute;left:279px;top:2px;width:102px;height:28px;border-radius:16px;background:var(--blue);color:var(--white);font-size:12px;padding:6px 0 0 18px}
.signup .go{position:absolute;left:351px;top:1px;width:30px;height:30px;border-radius:50%;background:#174e8c;display:flex;align-items:center;justify-content:center}

/* footer */
.footer-shape{position:absolute;left:0;top:2183px}
.footer-col{position:absolute;top:2285px;color:var(--white)}
.footer-col h3{font-family:"Lato",sans-serif;font-weight:700;font-size:17px;letter-spacing:.5px;margin-bottom:22px}
.footer-col ul{list-style:none;font-size:12px}
.footer-col li{height:31px;display:flex;gap:10px;align-items:flex-start}
.footer-col li::before{content:"»";font-weight:700}
.contact-list li::before{content:none}
.contact-list li{gap:14px;height:auto;margin-bottom:14px;line-height:20px}
.footer-bar{position:absolute;left:0;top:2495px;width:1200px;height:76px;background:var(--blue-deep)}
.copyright{position:absolute;left:100px;top:28px;font-size:12px;color:var(--white)}
.social{position:absolute;left:925px;top:19px;display:flex;gap:14px}
.social span{width:33px;height:33px;border-radius:50%;background:var(--white)}
</style>
</head>
<body>

<header class="site-header">
  <a class="brand" href="#"><span class="brand-square"></span><span class="brand-name">BIRCHWELL HOLDINGS</span></a>
  <div class="header-phone">
    <svg width="14" height="14" viewBox="0 0 24 24"><path fill="#0455a3" d="M6.6 10.8a15.1 15.1 0 0 0 6.6 6.6l2.2-2.2c.3-.3.7-.4 1-.2 1.1.4 2.3.6 3.6.6.6 0 1 .4 1 1V20c0 .6-.4 1-1 1A17 17 0 0 1 3 4c0-.6.4-1 1-1h3.5c.6 0 1 .4 1 1 0 1.3.2 2.5.6 3.6.1.3 0 .7-.2 1z"/></svg>
    (310) 555-0142
  </div>
  <a class="btn btn-quote" href="#">GET A QUOTE</a>
  <nav class="main-nav">
    <a class="active" href="#">HOME</a>
    <a href="#">BIRCHWELL TEAM</a>
    <a href="#">SERVICES</a>
    <a href="#">SOLD PROPERTIES</a>
    <a href="#">CONTACT</a>
  </nav>
</header>

<section class="hero">
  <div class="hero-photo" role="img" aria-label="Bright modern office lobby with framed art on a grey wall and tall glass doors"></div>
  <h1 class="hero-title">BIRCHWELL HOLDINGS</h1>
  <p class="hero-sub">We are a small boutique commercial real estate company.</p>
  <a class="btn-ghost" href="#">READ MORE</a>
  <div class="slider-arrow" style="left:28px"><svg width="10" height="12" viewBox="0 0 10 12"><path d="M7 1 2 6l5 5" stroke="#fff" stroke-width="2" fill="none"/></svg></div>
  <div class="slider-arrow" style="left:1138px"><svg width="10" height="12" viewBox="0 0 10 12"><path d="M3 1l5 5-5 5" stroke="#fff" stroke-width="2" fill="none"/></svg></div>
  <div class="slider-dots"><span class="on"></span><span></span><span></span><span></span></div>
  <svg class="hero-edge" viewBox="0 0 1200 630" preserveAspectRatio="none">
    <path d="M0 530 L600 630 L1200 520 L1200 630 L0 630 Z" fill="#fff"/>
    <path d="M0 530 L600 625 L1200 520" stroke="#0455a3" stroke-width="5" fill="none"/>
  </svg>
</section>

<section class="about">
  <h2 class="section-title about-title">ABOUT BIRCHWELL HOLDINGS</h2>
  <div class="about-photo" role="img" aria-label="Broker meeting with a couple of clients in a bright office"></div>
  <p class="about-text">Birchwell Holdings is a commercial real estate brokerage firm that provides a range of services to assist each of our clients in reaching their real estate objectives quickly and efficiently. Our focus on Southern California investment properties allows us to have a unique and focused perspective on this highly competitive market.</p>
  <a class="btn btn-more" href="#">READ MORE</a>
</section>

<form class="analysis">
  <h2>REQUEST A MARKET ANALYSIS<br>OF THEIR PROPERTY</h2>
  <div class="field" style="top:155px">Name*</div>
  <div class="field" style="top:211px">Property Address*</div>
  <div class="field" style="top:268px">Email Address</div>
  <div class="field" style="top:324px">Phone Number</div>
  <p class="req">* Required</p>
  <div class="btn btn-submit">SUBMIT</div>
</form>

<section class="news">
  <h2 class="news-head">LATEST CRE NEWS</h2>
  <svg class="abs" style="left:100px;top:1547px" width="1000" height="453" viewBox="0 0 1000 453">
    <path d="M0 0 H1000 V332 L500 453 L0 332 Z" fill="#f3f3f5"/>
  </svg>
  <div class="news-body">
    <div class="scroll-track"></div>
    <div class="scroll-thumb"></div>
    <article class="news-item" style="top:38px">
      <div class="news-thumb logo">Plazowire</div>
      <h3 class="news-title">PLAZOWIRE RELEASES 2017 MID-YEAR REPORT</h3>
      <p class="news-excerpt">Plazowire Releases 2017 Mid-Year Report Report features research, analysis and commercial real ...</p>
      <p class="news-date">Oct 18, 2017 1:00 PM</p>
      <a class="news-more" href="#">READ MORE <svg width="12" height="12" viewBox="0 0 12 12"><circle cx="6" cy="6" r="6" fill="#0455a3"/><path d="M5 3.5 7.5 6 5 8.5" stroke="#fff" stroke-width="1.5" fill="none"/></svg></a>
    </article>
    <article class="news-item" style="top:191px">
      <div class="news-thumb city" role="img" aria-label="Aerial view of downtown towers and a city park"></div>
      <h3 class="news-title" style="font-weight:400">'A MAJOR DISTRACTION': IS A MEGA-DEAL LIKE NORVELA'S ...</h3>
      <p class="news-excerpt">On a wall in Dale Hensick's office is a frame with a custom-engraved wrench and a photo of workers ...</p>
      <p class="news-date">Oct 18, 2017 8:52 AM</p>
      <a class="news-more" href="#">READ MORE <svg width="12" height="12" viewBox="0 0 12 12"><circle cx="6" cy="6" r="6" fill="#0455a3"/><path d="M5 3.5 7.5 6 5 8.5" stroke="#fff" stroke-width="1.5" fill="none"/></svg></a>
    </article>
  </div>
  <a class="btn btn-news" href="#">VIEW ALL NEWS</a>
</section>

<section class="newsletter">
  <h2 class="section-title news-title-lg">SIGN UP FOR OUR NEWSLETTER</h2>
  <p class="newsletter-sub">Stay informed on Plazowire happenings, including upcoming events and information.</p>
  <div class="signup">
    <span>Enter Email Address</span>
    <div class="send">Send</div>
    <div class="go"><svg width="12" height="12" viewBox="0 0 12 12"><path d="M3 1l6 5-6 5z" fill="#fff"/></svg></div>
  </div>
</section>

<footer>
  <svg class="footer-shape" width="1200" height="312" viewBox="0 0 1200 312">
    <path d="M0 57 L600 0 L1200 57 V312 H0 Z" fill="#0455a3"/>
  </svg>
  <div class="footer-col" style="left:100px">
    <h3>CONTACT US</h3>
    <ul class="contact-list">
      <li><svg width="14" height="18" viewBox="0 0 14 18"><path d="M7 1a6 6 0 0 1 6 6c0 4-6 10-6 10S1 11 1 7a6 6 0 0 1 6-6z" stroke="#fff" fill="none" stroke-width="1.4"/><circle cx="7" cy="7" r="2" stroke="#fff" fill="none"/></svg><span>4820 Larkmoor Ave. Ste 300<br>Los Angeles, CA 90025</span></li>
      <li><svg width="14" height="14" viewBox="0 0 24 24"><path fill="none" stroke="#fff" stroke-width="2" d="M6.6 10.8a15.1 15.1 0 0 0 6.6 6.6l2.2-2.2c.3-.3.7-.4 1-.2 1.1.4 2.3.6 3.6.6.6 0 1 .4 1 1V20c0 .6-.4 1-1 1A17 17 0 0 1 3 4c0-.6.4-1 1-1h3.5c.6 0 1 .4 1 1 0 1.3.2 2.5.6 3.6.1.3 0 .7-.2 1z"/></svg><span>(310) 555-0142</span></li>
      <li><svg width="15" height="12" viewBox="0 0 15 12"><rect x="1" y="1" width="13" height="10" fill="none" stroke="#fff" stroke-width="1.3"/><path d="M1 1l6.5 5.5L14 1" fill="none" stroke="#fff" stroke-width="1.3"/></svg><span>hello@teamdurnio.com</span></li>
    </ul>
  </div>
  <div class="footer-col" style="left:458px">
    <h3>COMPANY</h3>
    <ul><li>Home</li><li>Birchwell Team</li><li>Our Services</li><li>Sold Properties</li></ul>
  </div>
  <div class="footer-col" style="left:706px">
    <h3>OTHER LINKS</h3>
    <ul><li>Contact us</li><li>Book A Callback</li><li>FAQs</li><li>Terms &amp; Conditions</li></ul>
  </div>
  <div class="footer-col" style="left:972px">
    <h3>RESOURCES</h3>
    <ul><li>Our News</li><li>Blog Post</li><li>Property Details</li><li>Privacy Policy</li></ul>
  </div>
  <div class="footer-bar">
    <p class="copyright">© Copyright 2017 Birchwell Holdings. All Rights Reserved</p>
    <div class="social" aria-label="Social links"><span></span><span></span><span></span><span></span></div>
  </div>
</footer>

</body>
</html>
```